Meadowlark Counseling Partners, LLC Needs Modern Business Card Design.

We provide behavioral health services from western Kansas to eastern Kansas. There is an abundance of competition for the services we provide with our main competitor being larger and having significantly more financial resources; however, the quality of services we provide is greater and we have started to catch the attention of the State of Kansas. We had a great logo designed by ArtFolio - this will be used to build upon our brand. The logo (attached) should be used in the card development. We want something unique, modern, but also a card design that clearly states our name, contact info, provides the name and unqiue location of each clinician, etc. Rounded edges, or a unique size, just something that makes our business card stand out from others. I have also uploaded each clinician's name and their unique location and phone number.

Our idea is to have one side be black with our logo. Then, on the other side have business cards for each individual. Plus, we want one card that is "generic" with no specific clinician's name listed so that we can give clients an appointment card when they leave. Some clinicians have two locations - we're open to design and background color, but we have started going with branding colors of black, the yellow in the logo files attached, and sometimes a gray. Our new office has been decorated using this theme.

Target Market(s)

individuals and families in need of behavioral health services; potential professional referral sources; existing referral sources

Industry/Entity Type

Business

Contact Information for Business Card

I attached a Word doc that provides clinician names, credentials and location information specific to each individual.

Font styles to use
Serif

Colors
000000
fbed22
dbdbdb
9d9d9d
c3c3c3

Requirements
Must have
• 1) use of the company logo that has been attached; 2) a template that provides us space to individualize business cards for all of our clinicians; 3) should stick to the colors we are branding with: black, yellow from the logo file, maybe a gray shade and we're open to a suggestion on a shade of white.
Nice to have
• Group discussion culminated in the thought that one side would be black with just our logo - no clinician names, etc. A unique design - rounded edges, unique size, some catchy lay-out would be nice.
Should not have
• Must not be too busy. Should look "clean." The project should stick to branding colors: black, yellow (from the logo file), maybe a gray and shade of white.

```html
<!DOCTYPE html>
<html lang="en">
<head>
<meta charset="utf-8">
<title>Meadowlark Counseling Partners – Business Card</title>
<link href="https://fonts.googleapis.com/css2?family=Open+Sans:wght@400;600;700&display=swap" rel="stylesheet">
<style>
  :root {
    --black: #000000;
    --card-black: #050608;
    --yellow: #fbed22;
    --amber: #fbb022;
    --gold: #f2b81c;
    --paper: #e4e4e4;
    --paper-light: #ececec;
    --gray-mid: #c3c3c3;
    --gray-dark: #9d9d9d;
    --stage: #d9d9d9;
    --ink: #111111;
  }
  * { box-sizing: border-box; margin: 0; padding: 0; }
  html, body {
    width: 1200px; height: 1000px; overflow: hidden;
    background: var(--stage);
    font-family: "Open Sans", Arial, sans-serif;
  }
  .canvas {
    width: 1200px; height: 1000px;
    display: flex; align-items: center; justify-content: center; gap: 80px;
  }
  .card {
    width: 400px; height: 620px;
    border-radius: 56px;
    position: relative; overflow: hidden;
    box-shadow: 0 6px 18px rgba(0,0,0,0.18);
  }
  .card--front {
    background: linear-gradient(180deg, var(--paper-light), var(--paper));
  }
  .card--back { background: var(--card-black); }

  .info-band {
    position: absolute; left: 0; right: 0; top: 150px; height: 210px;
    background: linear-gradient(90deg, var(--amber) 0%, #fbcf22 55%, var(--yellow) 100%);
    display: flex; flex-direction: column; align-items: center;
    padding-top: 26px; color: var(--ink);
  }
  .clinician-name { font-size: 27px; font-weight: 700; line-height: 1.1; }
  .clinician-title { font-size: 17px; font-weight: 400; margin-top: 2px; }
  .locations {
    display: flex; margin-top: 34px; font-size: 15.5px; line-height: 1.3;
  }
  .location { padding: 0 6px; white-space: nowrap; }
  .location--primary { text-align: right; border-right: 1px solid rgba(0,0,0,0.45); }
  .location--secondary { text-align: left; }

  .front-mark {
    position: absolute; left: 0; right: 0; bottom: 50px;
    display: flex; flex-direction: column; align-items: center; gap: 10px;
    color: var(--gray-mid); font-size: 13px; font-weight: 600;
  }
  .front-mark .dot {
    width: 46px; height: 46px; border-radius: 50%; background: var(--gray-mid);
  }

  .brand {
    position: absolute; left: 0; right: 0; top: 270px;
    display: flex; flex-direction: column; align-items: center; gap: 16px;
    color: var(--gold);
  }
  .brand .dot {
    width: 54px; height: 54px; border-radius: 50%; background: var(--gold);
  }
  .brand-name {
    font-size: 17px; font-weight: 600; letter-spacing: 1px;
    text-transform: uppercase; text-align: center; line-height: 1.35;
  }
</style>
</head>
<body>
<main class="canvas">
  <section class="card card--front" aria-label="Clinician side">
    <div class="info-band">
      <p class="clinician-name">Daniel R. Hollis, LP</p>
      <p class="clinician-title">President</p>
      <div class="locations">
        <address class="location location--primary">418 N. Elm St.<br>Wichita, Kansas 67203<br>(316) 555-0142</address>
        <address class="location location--secondary">209 W. Main St., Ste. 104<br>Parsons, Kansas 67351<br>(844) 555-0187</address>
      </div>
    </div>
    <div class="front-mark">
      <span class="dot"></span>
      <span>Meadowlark Counseling Partners, LLC</span>
    </div>
  </section>

  <section class="card card--back" aria-label="Brand side">
    <div class="brand">
      <span class="dot"></span>
      <p class="brand-name">Meadowlark<br>Counseling Partners, LLC</p>
    </div>
  </section>
</main>
</body>
</html>
```